Flyer for home based dog grooming salon

I need a flyer design for my home based dog grooming business. This flyer will be used for letterbox drops and supplied to local businesses such as vets. I may also extend the design at a later date for business cards as well.
Key advantages I want highlighted are listed below. They are listed in order of importance so that if the flyer becomes too busy, the less important items can be left off:
- "one on one personalised service where the groomer listens to your needs"
- NO CAGING...pets groomed immediately
- the same groomer for your pet at each groom, making your pet more comfortable
- local business in Gordon Park
- modern, air-conditioned salon
- VIP program offering discounts for regular clients
List of services to be included are listed below:
- tidy-ups
- full-body clipping
- strip-outs
- breed specific clips
- and more...
Phone number, website and email address all need to be indicated clearly so they stand out
0455 862 914 (use the spacing as shown)
www.marlowfieldtrims.com.au
info@marlowfieldtrims.com.au
I have no strong preferences for colours, however, as I am a male groomer, I don't want the flyer to be too feminine but also not too masculine as many of the prospective customers are female.
I have seen good examples of flyers with images of dogs being groomed on them and flyers with just images of dogs on them and I have no preference for either - it will depend on the overall look of the flyer. If you wish to include images of dogs being groomed, I have uploaded 38 images of dogs being groomed taken from my salon. I don't want images of anyone else grooming dogs on the flyer. As i cater to all size dogs, any images of dogs do not need to limited to small breeds.
The flyer size will be DL (99 x 210 mm) and can be single or double sided. If you plan on doing double sided, please ensure the list of services offered is shown on the front side.
As an example of several designs I have seen before, in 2012 there was a project for Hollisvale Groomers. From designs submitted, I liked #1135917, #1137543, #1135911 and probably would have gone for #1140593. I did not like the winner.
Dog owners
Salon

```html
<!DOCTYPE html>
<html lang="en">
<head>
<meta charset="utf-8">
<title>Marlowfield Trims – Flyer</title>
<link href="https://fonts.googleapis.com/css2?family=Sniglet:wght@400;800&family=Delius&family=Tinos:wght@700&display=swap" rel="stylesheet">
<style>
  :root {
    --page: #ececea;
    --ink: #1c1b1e;
    --mint: #d4efc3;
    --leaf: #8db66b;
    --plum: #4a3f56;
    --violet: #6f5fa8;
    --paw: #54506a;
    --white: #f4f4f2;
  }
  * { margin: 0; padding: 0; box-sizing: border-box; }
  html, body { width: 1200px; height: 900px; overflow: hidden; background: var(--page); }
  .flyer {
    position: absolute; left: 50px; top: 190px;
    width: 1100px; height: 520px; overflow: hidden;
    background: var(--ink);
    box-shadow: 0 6px 18px rgba(0,0,0,.18);
  }
  .flyer-art { position: absolute; inset: 0; }
  .tagline {
    position: absolute; left: 56px; top: 170px;
    font-family: "Delius", cursive; font-size: 32px; line-height: 37px;
    color: var(--white); transform: rotate(-5.1deg); transform-origin: left top;
  }
  .tagline .lead { color: var(--mint); }
  .services {
    position: absolute; right: 400px; top: 108px; text-align: right;
    font-family: "Sniglet", cursive; font-size: 23px; line-height: 30px;
    color: var(--leaf); transform: rotate(-5.1deg); transform-origin: right top;
  }
  .services h2 { font-weight: 400; font-size: 25px; line-height: 32px; color: var(--mint); }
  .services li { list-style: none; }
  .services li::after {
    content: ""; display: inline-block; width: 16px; height: 14px; margin-left: 8px;
    background: radial-gradient(circle at 50% 70%, var(--violet) 5px, transparent 5.5px);
  }
  .brand {
    position: absolute; left: 84px; top: 396px;
    font-family: "Sniglet", cursive; font-weight: 800; font-size: 42px; line-height: 50px; letter-spacing: 2px;
    color: var(--leaf); transform: rotate(-5.1deg); transform-origin: left top;
  }
  .contact {
    position: absolute; left: 84px; top: 466px;
    font-family: "Tinos", serif; font-weight: 700; color: var(--mint);
    transform: rotate(-5.1deg); transform-origin: left top;
  }
  .contact .phone { font-size: 26px; line-height: 28px; letter-spacing: 1px; }
  .contact .links { font-size: 15px; line-height: 18px; display: flex; gap: 20px; align-items: center; margin-top: 2px; }
  .contact .links span { display: flex; align-items: center; gap: 6px; }
  .contact svg { width: 13px; height: 13px; }
</style>
</head>
<body>
<div class="flyer">
  <svg class="flyer-art" viewBox="0 0 1100 520" width="1100" height="520">
    <defs>
      <linearGradient id="groomerTone" x1="0" y1="0" x2="1" y2="1">
        <stop offset="0" stop-color="#d9c2b2"/><stop offset="1" stop-color="#6b6260"/>
      </linearGradient>
      <radialGradient id="dogTone" cx=".45" cy=".4" r=".7">
        <stop offset="0" stop-color="#f3f1ee"/><stop offset=".7" stop-color="#d8d4cf"/><stop offset="1" stop-color="#9c9792"/>
      </radialGradient>
    </defs>
    <g class="paws" fill="var(--paw)" opacity=".8">
      <g transform="translate(330 95)"><ellipse cx="0" cy="8" rx="9" ry="7"/><circle cx="-9" cy="-4" r="3.5"/><circle cx="-3" cy="-9" r="3.5"/><circle cx="4" cy="-9" r="3.5"/><circle cx="10" cy="-4" r="3.5"/></g>
      <g transform="translate(400 140)"><ellipse cx="0" cy="8" rx="9" ry="7"/><circle cx="-9" cy="-4" r="3.5"/><circle cx="-3" cy="-9" r="3.5"/><circle cx="4" cy="-9" r="3.5"/><circle cx="10" cy="-4" r="3.5"/></g>
      <g transform="translate(290 150)"><ellipse cx="0" cy="8" rx="9" ry="7"/><circle cx="-9" cy="-4" r="3.5"/><circle cx="-3" cy="-9" r="3.5"/><circle cx="4" cy="-9" r="3.5"/><circle cx="10" cy="-4" r="3.5"/></g>
    </g>
    <g class="photo-groomer">
      <rect x="430" y="-20" width="380" height="122" rx="50" fill="var(--mint)"/>
      <rect x="442" y="-20" width="356" height="110" rx="44" fill="url(#groomerTone)" role="img" aria-label="Photo of the groomer holding a small white dog in the salon"/>
    </g>
    <g class="photo-dog">
      <circle cx="945" cy="85" r="232" fill="var(--mint)"/>
      <circle cx="945" cy="85" r="216" fill="url(#dogTone)" role="img" aria-label="Photo of a freshly groomed small white dog"/>
    </g>
    <path class="band-name" d="M0 390 L1100 290 L1100 520 L0 520 Z" fill="var(--mint)"/>
    <path class="band-contact" d="M0 458 L1100 358 L1100 520 L0 520 Z" fill="var(--plum)"/>
  </svg>

  <p class="tagline"><span class="lead">One On one</span><br>personalised service<br>where the groomer<br>listens to your needs</p>

  <div class="services">
    <h2>our Services include</h2>
    <ul>
      <li>tidy-ups</li>
      <li>full-body clipping</li>
      <li>strip-outs</li>
      <li>breed specific clips</li>
      <li>and more...</li>
    </ul>
  </div>

  <div class="brand">Marlowfield Trims</div>

  <div class="contact">
    <div class="phone">0455 862 914</div>
    <div class="links">
      <span><svg viewBox="0 0 14 14"><rect x="1" y="3" width="12" height="8" fill="none" stroke="currentColor" stroke-width="1.5"/><path d="M1 3 L7 8 L13 3" fill="none" stroke="currentColor" stroke-width="1.5"/></svg>info@marlowfieldtrims.com.au</span>
      <span><svg viewBox="0 0 14 14"><circle cx="7" cy="7" r="5.5" fill="none" stroke="currentColor" stroke-width="1.5"/><path d="M1.5 7 H12.5 M7 1.5 C4 5 4 9 7 12.5 C10 9 10 5 7 1.5" fill="none" stroke="currentColor" stroke-width="1.2"/></svg>www.marlowfieldtrims.com.au</span>
    </div>
  </div>
</div>
</body>
</html>
```